Talented energy healer needs business card design

I need a business card design for a new energy healing business in Perth Australia. As an energy healer I am quite earthy and practical rather than floaty and fairydust.
One of the techniques I use is unique in Australia but used internationally (US, UK and Europe). I practice with Coastal Pathway Method, Reiki and massage as well as some other techniques I developed personally. I am starting to incorporate sound healing into my practice. I literally change people's lives. The potential for each client is wide open. A key skill I bring to my practice is the capacity for making difficult situations seem more fun and less stressful.
Clients are likely to be depressed, physically unwell, going through a difficult time, unhappy with their current situation. They are people looking for new options to solve a difficult existing problem. They have probably tried other avenues before they come to me. They are open to something different.

I would like to communicate that the client and I work together for their healing and personal growth. I would like to convey that while the work of changing is challenging it can also be fun.
Updates

Hi all, info required on the card is:

Name
Title: Healer
contact number (mobile)
I don''t have a logo - I would be interested in seeing designs that use the whole card as well as the traditional logo on one side / in one corner. Whatever ''look/feel'' I choose will carry over to the website as well.

thanks
Meg

Reason: One or two of the designs caught my eye and many appeal for different reasons, but nothing is quite right for me. I've invited a couple of other designers to contribute so I wanted to give them time to be involved. kind regards Meg

Thank you all for the fabulous designs. I really appreciated the thought that many people put into my brief and a number of designs captured important things about what I was trying to say. It was a hard choice between 3 designs in the end.
thanks again and kind regards
Meg

Target Market(s)

people looking for new options to solve a difficult existing problem

Industry/Entity Type

Massage

Logo styles of interest
Abstract Logo
Requirements
Must have
• include green and blue
Nice to have
• hands, tea / teapots , the ocean, stepping stones

```html
<!DOCTYPE html>
<html lang="en">
<head>
<meta charset="utf-8">
<title>Meg – Energy Healer business card</title>
<link rel="stylesheet" href="https://fonts.googleapis.com/css2?family=Uncial+Antiqua&family=Dancing+Script:wght@400&family=Bodoni+Moda:opsz,wght@6..96,700&display=swap">
<style>
  :root {
    --page: #ffffff;
    --ink: #000000;
    --deep-blue: #0a2fd6;
    --bright-blue: #1f6bff;
    --cyan: #35d2f0;
    --green: #3fe07a;
    --night: #030506;
    --sepia-dark: #3a1f0e;
    --sepia-light: #d9c7ae;
    --glow: #ffffff;
  }
  html, body {
    margin: 0;
    padding: 0;
    overflow: hidden;
    background: var(--page);
  }
  .canvas {
    position: relative;
    width: 1200px;
    height: 718px;
    background: var(--page);
    overflow: hidden;
  }
  .card-art {
    position: absolute;
    inset: 0;
  }
  .service-title {
    position: absolute;
    left: 0;
    top: 0;
    margin: 0;
    font-family: "Dancing Script", cursive;
    font-weight: 400;
    color: var(--glow);
    line-height: 1;
    text-shadow: 0 0 6px var(--glow), 0 0 14px rgba(255,255,255,0.7);
  }
  .service-title span {
    position: absolute;
    white-space: nowrap;
    transform-origin: left top;
  }
  .service-title .line-one {
    left: 626px;
    top: 140px;
    font-size: 136px;
    transform: rotate(-4deg) scaleX(1.45);
  }
  .service-title .line-two {
    left: 640px;
    top: 240px;
    font-size: 132px;
    transform: rotate(-4deg) scaleX(1.4);
  }
  .healer-name {
    position: absolute;
    left: 146px;
    top: 448px;
    margin: 0;
    font-family: "Uncial Antiqua", serif;
    font-size: 74px;
    line-height: 1;
    text-transform: uppercase;
    color: var(--ink);
    text-shadow: 0 0 6px var(--glow), 0 0 12px var(--glow), 0 0 18px var(--glow);
  }
  .contact-line {
    position: absolute;
    left: 184px;
    top: 556px;
    margin: 0;
    font-family: "Bodoni Moda", serif;
    font-weight: 700;
    font-size: 52px;
    line-height: 1;
    color: var(--ink);
    transform: scaleX(0.74);
    transform-origin: left top;
    text-shadow: 0 0 6px var(--glow), 0 0 12px var(--glow), 0 0 18px var(--glow);
    white-space: nowrap;
  }
  .contact-line .divider {
    margin: 0 44px;
  }
</style>
</head>
<body>
<main class="canvas">
  <svg class="card-art" width="1200" height="718" viewBox="0 0 1200 718">
    <defs>
      <linearGradient id="sky-band" x1="0" y1="0" x2="0" y2="1">
        <stop offset="0" stop-color="var(--deep-blue)"/>
        <stop offset="0.18" stop-color="var(--bright-blue)"/>
        <stop offset="0.34" stop-color="var(--night)"/>
        <stop offset="1" stop-color="var(--night)"/>
      </linearGradient>
      <radialGradient id="energy-wash" cx="0.92" cy="0.9" r="0.85">
        <stop offset="0" stop-color="var(--green)" stop-opacity="0.75"/>
        <stop offset="0.45" stop-color="#3ec8d8" stop-opacity="0.45"/>
        <stop offset="0.8" stop-color="var(--cyan)" stop-opacity="0.15"/>
        <stop offset="1" stop-color="var(--cyan)" stop-opacity="0"/>
      </radialGradient>
      <linearGradient id="hands-tone" x1="0" y1="0" x2="1" y2="1">
        <stop offset="0" stop-color="var(--sepia-light)"/>
        <stop offset="0.45" stop-color="#8a5a34"/>
        <stop offset="1" stop-color="var(--sepia-dark)"/>
      </linearGradient>
      <filter id="soft-glow" x="-20%" y="-20%" width="140%" height="140%">
        <feGaussianBlur stdDeviation="6"/>
      </filter>
      <clipPath id="card-shape">
        <rect x="42" y="37" width="1114" height="639" rx="74"/>
      </clipPath>
    </defs>

    <g class="card-face" clip-path="url(#card-shape)">
      <rect x="42" y="37" width="1114" height="639" fill="url(#sky-band)"/>
      <rect class="energy-pattern" role="img" aria-label="Abstract blue and green ripple pattern"
            x="42" y="37" width="1114" height="639" fill="url(#energy-wash)"/>
    </g>

    <rect class="card-border" x="42" y="37" width="1114" height="639" rx="74"
          fill="none" stroke="var(--ink)" stroke-width="6"/>

    <rect x="127" y="114" width="470" height="320" rx="36" fill="var(--glow)" filter="url(#soft-glow)" opacity="0.8"/>
    <rect class="hands-photo" role="img" aria-label="Sepia photograph of two hands shaping clay together over an open palm"
          x="127" y="114" width="470" height="320" rx="36"
          fill="url(#hands-tone)" stroke="var(--glow)" stroke-width="3"/>
  </svg>

  <h1 class="service-title">
    <span class="line-one">Energy</span>
    <span class="line-two">Healer</span>
  </h1>

  <p class="healer-name">Meg</p>

  <p class="contact-line">
    <span class="phone">0491 570 156</span><span class="divider">~</span><span class="website">TideTurnWellness.com.au</span>
  </p>
</main>
</body>
</html>
```